Your Road Counsel Billboard Design for Personal Injury Law Firm

Need a billboard design that we can use for different versions. 1400px X 400px jpeg or png
I have attached the logo and the attorney for the billboard. Attorney Dana Whitfield
Here is a link to our current website yourroadcounsel-example.com

HEADLINE: HIT BY A TRUCK?
SUBHEAD: NO FEE. BIG FIGHT.
855-MARGOT-7

HEADLINE: ACCIDENT?
SUBHEAD: NO FEE, UNLESS WE WIN!
855-MARGOT-7

HEADLINE: BIG TRUCK. BIG CASE.
SUBHEAD: YOU PAY $0 UPFRONT
855-MARGOT-7

Target Market(s)

People in Car Accident

Industry/Entity Type

Personal Injury Attorneys

```html
<!DOCTYPE html>
<html lang="en">
<head>
<meta charset="utf-8">
<title>Your Road Counsel – Billboard</title>
<link rel="stylesheet" href="https://fonts.googleapis.com/css2?family=Montserrat:wght@600;700&display=swap">
<style>
  :root {
    --brand-green: #6bdc4b;
    --panel-navy: #1b1233;
    --text-white: #ffffff;
    --logo-grey: #5d5d63;
    --photo-light: #c9ccd0;
    --photo-mid: #8e9197;
    --photo-dark: #3c3d45;
  }
  * { margin: 0; padding: 0; box-sizing: border-box; }
  html, body {
    width: 1200px;
    height: 471px;
    overflow: hidden;
    background: var(--brand-green);
  }
  .billboard {
    position: relative;
    width: 1200px;
    height: 471px;
    background: var(--brand-green);
    font-family: "Montserrat", Arial, sans-serif;
  }
  .panel {
    position: absolute;
    left: 106px;
    top: 95px;
    width: 987px;
    height: 282px;
    background: var(--panel-navy);
    overflow: hidden;
  }
  .crash-photo {
    position: absolute;
    left: 621px;
    top: 0;
    width: 366px;
    height: 214px;
    background:
      linear-gradient(90deg, var(--panel-navy) 0%, rgba(27,18,51,0) 28%),
      linear-gradient(180deg, rgba(27,18,51,0) 78%, rgba(27,18,51,0.9) 100%),
      radial-gradient(ellipse at 62% 62%, var(--photo-dark) 0%, rgba(60,61,69,0) 38%),
      linear-gradient(100deg, var(--photo-dark) 0%, var(--photo-mid) 22%, var(--photo-light) 38%, var(--photo-mid) 55%, var(--photo-light) 80%, #b4b7bc 100%);
  }
  .copy {
    position: absolute;
    left: 42px;
    top: 48px;
  }
  .headline {
    color: var(--brand-green);
    font-weight: 700;
    font-size: 63px;
    line-height: 1;
    letter-spacing: -0.5px;
    white-space: nowrap;
  }
  .subhead {
    color: var(--text-white);
    font-weight: 600;
    font-size: 55px;
    line-height: 1;
    margin-top: 6px;
    letter-spacing: -0.5px;
    white-space: nowrap;
  }
  .phone {
    color: var(--brand-green);
    font-weight: 600;
    font-size: 69px;
    line-height: 1;
    margin-top: 6px;
    letter-spacing: -1px;
    white-space: nowrap;
  }
  .firm-badge {
    position: absolute;
    left: 658px;
    top: 172px;
    width: 282px;
    height: 69px;
    border: 1px solid var(--brand-green);
    background: var(--panel-navy);
    display: flex;
    align-items: center;
    justify-content: center;
  }
  .firm-name {
    color: var(--logo-grey);
    font-weight: 600;
    font-size: 20px;
    letter-spacing: 0.5px;
    text-transform: uppercase;
    white-space: nowrap;
  }
</style>
</head>
<body>
  <div class="billboard">
    <div class="panel">
      <div class="crash-photo" role="img" aria-label="Photo of a damaged silver car crushed at the front beside a white semi truck"></div>
      <div class="copy">
        <h1 class="headline">HIT BY A TRUCK?</h1>
        <p class="subhead">NO FEE. BIG FIGHT.</p>
        <p class="phone">855-MARGOT-7</p>
      </div>
      <div class="firm-badge">
        <span class="firm-name">Your Road Counsel</span>
      </div>
    </div>
  </div>
</body>
</html>
```